Wordpress Design Project For Budget Hotel

Although it is a budget hotel we would like a mid to upmarket word press web design with relatively prominent images of local attractions. The design needs to be clean and professional looking.

This is design only. The design/files most be easy for our developer to work with and develop the back end/code.

The website will contain 6 pages:
Homepage
Accommodation & Rates
Facilities
Attractions
Bookings
Contact us

The full content is provided in a word doc which i have uploaded along with all the images needed.

Target Market(s)

The target audience are budget travelers looking for clean and comfortable accommodation at an affordable price.

Industry/Entity Type

Hotel

Requirements
Must have
• Prominent images of local attractions in a changing background or as a sliding banner.

Bookwell Hotel Reservation booking form. A small one on the home page and full one on the booking page.

Google maps window in the contact page
Should not have
• We dont want to many bright colours (ie yellow, red) but clean white is fine

```html
<!DOCTYPE html>
<html lang="en">
<head>
<meta charset="utf-8">
<title>Summit Hotel, Ridgeway</title>
<link href="https://fonts.googleapis.com/css2?family=Courgette&family=Arimo:wght@400;700&family=Crimson+Text:wght@400;600&display=swap" rel="stylesheet">
<style>
:root{
  --page-bg:#7fa6d3;
  --sheet:#fdfdfd;
  --ink:#2b2b2b;
  --muted:#555;
  --nav:#666;
  --brown:#6b3a0a;
  --navy:#1d2f45;
  --frame:#d4d4d4;
  --footer:#454545;
  --gold1:#e8e4a8;
  --gold2:#b7b064;
}
*{box-sizing:border-box;margin:0;padding:0}
html,body{width:1045px;height:1200px;overflow:hidden}
body{background:var(--page-bg);font-family:Arimo,Arial,sans-serif;color:var(--ink);position:relative}
.sheet{position:absolute;left:83px;top:0;width:879px;height:1200px;background:var(--sheet);box-shadow:0 0 6px rgba(0,0,0,.25)}
.brand{position:absolute;left:22px;top:42px;font-family:Courgette,cursive;font-size:20px;color:var(--navy)}
.nav{position:absolute;right:34px;top:39px;display:flex;font-size:12.5px;font-weight:700;color:var(--nav)}
.nav span{padding:10px 12px}
.nav .active{background:#efefef}
.hero{position:absolute;left:0;top:105px;width:879px;height:330px;background:linear-gradient(180deg,#5f9ad8 0%,#dfe9f2 30%,#7d9bb1 46%,#2e5a2c 70%,#6b6a5e 100%)}
.hero-caption{position:absolute;left:0;bottom:0;width:100%;height:35px;background:rgba(0,0,0,.45);color:#eee;font-size:12px;padding:12px 9px}
.welcome{position:absolute;left:0;width:630px;top:473px;text-align:center;font-family:Courgette,cursive;font-size:21px;color:var(--brown)}
.check-btn{position:absolute;left:605px;top:470px;width:173px;height:32px;border-radius:16px;background:linear-gradient(180deg,var(--gold1),var(--gold2));border:1px solid #9a9450;font-family:"Crimson Text",serif;font-weight:600;font-variant:small-caps;font-size:21px;color:#2f3a20;text-align:center;line-height:30px}
.photo{position:absolute;left:22px;width:240px;height:170px;border:1px solid var(--frame);background:#fff;padding:7px;box-shadow:0 1px 2px rgba(0,0,0,.12)}
.photo div{width:100%;height:100%}
.room{background:linear-gradient(160deg,#e9e7e2,#c9c6bf 60%,#3a3a3a)}
.lounge{background:linear-gradient(160deg,#dcdcd2,#8c8c80 50%,#b11e24 75%,#2a2a2a)}
.falls{background:linear-gradient(180deg,#4c6a34,#8a7650 45%,#cfd5d8 60%,#3d5a2a)}
.item{position:absolute;left:303px;width:270px;font-size:12.5px;line-height:18px;color:var(--ink)}
.item h2{font-family:Courgette,cursive;font-weight:400;font-size:16px;color:var(--brown);margin:0 0 2px 40px}
.booking{position:absolute;left:601px;top:539px;width:246px;height:207px;border:1px solid #c9c9c9;border-radius:4px;background:#f4f4f4;font-family:"Crimson Text",serif;font-size:11.5px;color:#222;padding:12px 16px}
.field{display:flex;align-items:center;gap:4px;margin:1px 0 6px}
.field span{display:inline-block;width:72px;height:19px;border:1px solid #ccc;background:#fff;font-size:13px;padding:0 3px;line-height:18px}
.booking .nights{color:#666;font-size:10.5px;margin-bottom:8px}
.booking hr{border:0;border-top:1px solid #ccc}
.persons{padding:7px 0;font-size:12.5px;display:flex;align-items:center;gap:4px}
.persons span{display:inline-block;width:36px;height:16px;border:1px solid #bbb;background:#fff;font-size:10px;padding-left:3px}
.search{margin-top:17px;display:inline-block;border:1px solid #777;background:linear-gradient(#fff,#ddd);font-size:13px;padding:1px 9px}
.powered{position:absolute;right:14px;bottom:12px;font-size:8px;color:#888}
.weather{position:absolute;left:599px;top:786px;width:249px;height:295px;border:1px solid #ddd;border-radius:4px;background:#fff;padding:6px 12px;font-size:12.5px;line-height:18px;box-shadow:0 3px 4px rgba(0,0,0,.08)}
.weather h3{font-size:14.5px;color:var(--muted);margin-bottom:16px}
.wicon{width:40px;height:38px;border-radius:50%;background:radial-gradient(circle,#f5d64a 40%,#dfe3e8 70%);margin-bottom:14px}
.weather b{display:block}
.footer{position:absolute;left:0;top:1146px;width:879px;height:54px;background:var(--footer)}
.footer i{position:absolute;left:22px;right:22px;top:13px;border-top:1px solid #2f2f2f}
</style>
</head>
<body>
<div class="sheet">
  <div class="brand">Summit Hotel, RIDGEWAY</div>
  <div class="nav"><span class="active">Home</span><span>Accommodation &amp; Rates</span><span>Facilities</span><span>Attractions</span><span>Bookings</span><span>Contact us</span></div>
  <div class="hero" role="img" aria-label="Visitors on a wooden lookout above forested mountain ranges under a cloudy blue sky">
    <div class="hero-caption">Attractions</div>
  </div>
  <div class="welcome">Welcome to the Summit Hotel in Ridgeway.</div>
  <div class="check-btn">Check Availability</div>

  <div class="photo" style="top:541px"><div class="room" role="img" aria-label="Hotel bedroom with a made double bed"></div></div>
  <div class="item" style="top:562px"><h2>Accommodation &amp; Rates</h2>Enjoy the wonders of Ridgeway from only $70 per night.<br>1-2 people for $70.00<br>3 people for $95.00<br>Family 2+2 for $110.00</div>

  <div class="photo" style="top:730px"><div class="lounge" role="img" aria-label="Lounge with a red sofa and white coffee table"></div></div>
  <div class="item" style="top:755px"><h2>Hotel Facilities</h2>Lounge &amp; Horse Shoe Bar - One of the last great horseshoe bars with pool table and big screen TV for sports.</div>

  <div class="photo" style="top:917px"><div class="falls" role="img" aria-label="Waterfall dropping into a forested gorge"></div></div>
  <div class="item" style="top:943px"><h2>Attractions</h2>Fernhollow Falls<br>Ridgeway Steam Railway and Museum<br>World Heritage Ridgeway National Park<br>Golf ... and more</div>

  <div class="booking">
    Check-in:
    <div class="field"><span>08/31/2013</span><svg width="14" height="15"><rect x=".5" y="1.5" width="13" height="13" fill="#e6f0fb" stroke="#4a7fc0"/><rect x=".5" y="1.5" width="13" height="3" fill="#4a7fc0"/></svg></div>
    Check-out:
    <div class="field"><span>09/01/2013</span><svg width="14" height="15"><rect x=".5" y="1.5" width="13" height="13" fill="#e6f0fb" stroke="#4a7fc0"/><rect x=".5" y="1.5" width="13" height="3" fill="#4a7fc0"/></svg></div>
    <div class="nights">Nights: 1</div>
    <hr>
    <div class="persons">Number of persons: <span>1 ▾</span></div>
    <hr>
    <div class="search">Search »</div>
    <div class="powered">Powered by Bookwell</div>
  </div>

  <div class="weather">
    <h3>RIDGEWAY</h3>
    <div class="wicon" role="img" aria-label="Partly cloudy weather icon"></div>
    <b>Current Conditions:</b>Partly Cloudy, 70 F<br><br>
    <b>Forecast:</b>Sat - Clouds Early/Clearing Late. High: 75 Low: 54<br>Sun - Sunny. High: 74 Low: 54<br>Mon - Mostly Sunny. High: 72 Low: 55<br>Tue - Partly Cloudy. High: 72 Low: 52<br>Wed - Partly Cloudy. High: 72 Low: 51
  </div>

  <div class="footer"><i></i></div>
</div>
</body>
</html>
```